Create Flyer for RGB wall washers

We are launching a product that is run by an app and allows you to customize your exterior lighting at the touch of a button. We want to create the image of being technologically advanced company who is easy to work with. Looking for streamlined design which will reflect how we operate as a company. We will be printing at printmarrow.example so please have the correct format. I am looking for this to be single sided thank you for your time and submission

Target Market(s)

Residential and commercial

Industry/Entity Type

Product

Requirements
Must have
• clean layout
• easy to read
• Common fonts
• Color scheme must work with logo (we can provide a black background to logo in needed)
Nice to have
• Nicely displayed images to help sell the idea
Should not have
• Too busy background

```html
<!DOCTYPE html>
<html lang="en">
<head>
<meta charset="utf-8">
<title>Lumenfield Design – App-Controlled Outdoor Lighting Flyer</title>
<link rel="stylesheet" href="https://fonts.googleapis.com/css2?family=Ubuntu:wght@400;500;700&display=swap">
<style>
  :root {
    --stage: #d9dbde;
    --paper: #f3f4f6;
    --paper-shade: #e4e6ea;
    --navy: #2b2f7a;
    --ink: #2a2c33;
    --body-grey: #5b5e66;
    --accent-red: #d1202a;
    --brand-blue: #1f6fb6;
    --night-blue: #1d3556;
    --night-purple: #4a2d6e;
    --night-red: #5a1a24;
  }
  * { box-sizing: border-box; margin: 0; padding: 0; }
  html, body { width: 1200px; height: 959px; overflow: hidden; }
  body {
    background: var(--stage);
    font-family: "Ubuntu", Arial, sans-serif;
    position: relative;
  }
  .flyer {
    position: absolute;
    left: 100px; top: 146px;
    width: 1000px; height: 667px;
    background: linear-gradient(180deg, var(--paper) 0%, #ffffff 45%, var(--paper-shade) 100%);
    box-shadow: 0 6px 24px rgba(0,0,0,.18);
    overflow: hidden;
  }
  .headline {
    position: absolute; left: 36px; top: 24px; right: 36px;
    color: var(--navy); font-size: 30px; font-weight: 400; letter-spacing: .2px;
  }
  .headline strong { font-weight: 700; }
  .gallery {
    position: absolute; left: 36px; right: 36px; top: 78px; height: 330px;
    display: grid; grid-template-columns: 1fr 1fr 1fr; gap: 12px;
  }
  .scene {
    position: relative; color: #fff; text-align: center;
    font-size: 17px; line-height: 1.25; padding-top: 18px;
  }
  .scene--everyday { background: linear-gradient(180deg, var(--night-blue) 0%, #33324a 55%, #4b3b3a 100%); }
  .scene--events { background: linear-gradient(180deg, #231a33 0%, var(--night-purple) 50%, #3a4aa0 85%, #7a2c55 100%); }
  .scene--holiday { background: linear-gradient(180deg, #172544 0%, var(--night-red) 55%, #2b5a3f 100%); }
  .app-preview {
    position: absolute; left: 36px; top: 430px; width: 300px; height: 130px;
    background: linear-gradient(90deg, #cfd3d9, #eef0f3 50%, #cfd3d9);
  }
  .pitch { position: absolute; left: 370px; top: 432px; right: 36px; }
  .pitch-lead { color: var(--navy); font-size: 20px; line-height: 1.3; }
  .pitch-lead strong { font-weight: 700; }
  .pitch-body { color: var(--body-grey); font-size: 15.5px; line-height: 1.45; margin-top: 10px; }
  .footer {
    position: absolute; left: 0; right: 0; bottom: 0; height: 92px;
    display: flex; align-items: center; padding: 0 36px; gap: 60px;
    background: linear-gradient(180deg, rgba(255,255,255,0) 0%, var(--paper-shade) 100%);
  }
  .brand { display: flex; align-items: center; gap: 10px; color: var(--brand-blue); font-size: 24px; font-weight: 700; letter-spacing: .5px; }
  .brand-dot { width: 14px; height: 14px; border-radius: 50%; background: var(--brand-blue); }
  .offer { font-size: 16px; line-height: 1.55; }
  .offer-price { color: var(--ink); font-weight: 700; }
  .offer-contact { color: var(--accent-red); font-weight: 500; }
  .offer-contact .phone { font-weight: 700; margin-right: 14px; }
</style>
</head>
<body>
  <main class="flyer">
    <h1 class="headline">Control your outdoor lighting <strong>with the touch of a button</strong></h1>

    <section class="gallery">
      <div class="scene scene--everyday" role="img" aria-label="Stone house at night lit with soft white up-lights">
        <p>Standard lighting<br>for everyday use</p>
      </div>
      <div class="scene scene--events" role="img" aria-label="Stone house at night washed in purple, blue and pink light">
        <p>Special events<br>you choose the colors and effects</p>
      </div>
      <div class="scene scene--holiday" role="img" aria-label="House at night with red-lit tree and green-lit gable for the holidays">
        <p>Holiday lighting made simple</p>
      </div>
    </section>

    <div class="app-preview" role="img" aria-label="Row of smartphones showing the lighting control app with a colour wheel"></div>

    <section class="pitch">
      <p class="pitch-lead">Change the color or effect with the touch of a finger through <strong>an easy to use App from your phone or tablet</strong></p>
      <p class="pitch-body">State-of-the-Art lighting system that will wash your exterior walls with light or landscape plantings with up-lights. Its year-round lighting at a fraction of the cost.</p>
    </section>

    <footer class="footer">
      <div class="brand"><span class="brand-dot"></span>LUMENFIELD DESIGN</div>
      <div class="offer">
        <p class="offer-price">Prices starting at $799 including installation - this system is scalable.</p>
        <p class="offer-contact"><span class="phone">Call us today 555 014 2368</span>www.lumenfield-design.example</p>
      </div>
    </footer>
  </main>
</body>
</html>
```